stationary and business card
varkomo.de - online services platform
Project: stationary and business card
stationary and business card - Internet Services
Creative Brief
Modern
Dipl. Inf. Tobias Wendrich
Luvesor
Ulmenhain Str. 14 70386 Weil der Stadt
tobias.wendrich@mailhafen.de
www.varkomo.de
Please use logo colors, and see the following flyer to fit the style: varkomo.de/flyer.pdf
Für Dienstleister: * Kostenlose reservierungsplatform * Kostengunstige Flyer-Werbung * Kosten und Zeit für Anreise gleich bei Reservierung berechnen * Eigene varkomo.de Subdomain und Web- Seite mit einem SSL Zertifi kat * SMS Benachrichtigungen bei Reservierung 24 h Für Kunden: * 24 Stunden täglich online reservieren (z.B. Arzt, Massage, Friseur, uvm.) * Schnelle Abwicklung * Last-Minute-Preise und Frübucherrabatt möglich * Bewertungssystem für zuverlässige Dienstleister

```html
<!DOCTYPE html>
<html lang="de">
<head>
<meta charset="utf-8">
<title>varkomo.de – Geschäftsausstattung</title>
<link href="https://fonts.googleapis.com/css2?family=Open+Sans:wght@400;600;700&display=swap" rel="stylesheet">
<style>
  :root{
    --stage:#2b2b2d;
    --paper:#ffffff;
    --blue:#1b8fd4;
    --blue-light:#62c4ee;
    --green:#8cc43f;
    --ink:#2c2c2c;
    --muted:#8a8f95;
    --rule:#c9cdd2;
  }
  *{box-sizing:border-box;margin:0;padding:0}
  html,body{width:1200px;height:497px;overflow:hidden;background:var(--stage);font-family:"Open Sans",Arial,sans-serif;color:var(--ink)}
  .canvas{position:relative;width:1200px;height:497px}
  .sheet,.envelope,.card{position:absolute;background:var(--paper);overflow:hidden;box-shadow:0 2px 6px rgba(0,0,0,.5)}

  /* header band shared by sheets and envelope */
  .band{position:absolute;right:0;height:20px;background:linear-gradient(90deg,var(--blue-light),var(--blue));border-radius:14px 0 0 14px;color:#fff;font-size:5px;line-height:20px;padding-left:16px;white-space:nowrap}
  .band::after{content:"";position:absolute;left:6px;right:0;bottom:-4px;height:2px;background:var(--green);border-radius:2px 0 0 2px}
  .brand{position:absolute;display:flex;align-items:center;gap:5px;font-weight:700;color:var(--blue);white-space:nowrap}
  .brand .dot{border-radius:50%;background:var(--blue-light);flex:none}
  .brand small{display:block;font-size:.32em;font-weight:400;color:var(--muted);line-height:1}

  /* letterhead */
  .letterhead{left:24px;top:24px;width:331px;height:456px}
  .letterhead .band,.fax .band{top:22px;width:200px}
  .sheet .brand{left:16px;top:14px;font-size:16px}
  .sheet .brand .dot{width:24px;height:24px}
  .faint-mark{position:absolute;left:105px;top:205px;width:120px;height:120px;border-radius:50%;background:radial-gradient(circle,rgba(98,196,238,.16),rgba(140,196,63,.10));display:flex;align-items:center;justify-content:center;font-weight:700;font-size:17px;color:rgba(27,143,212,.14)}

  /* fax */
  .fax{left:384px;top:24px;width:331px;height:456px}
  .fax h1{position:absolute;left:16px;top:76px;font-size:24px;font-weight:400;letter-spacing:1px}
  .fax-fields{position:absolute;left:16px;top:118px;width:298px;display:grid;grid-template-columns:1fr 1fr;column-gap:18px;row-gap:9px}
  .field{font-size:5px;border-bottom:1px solid var(--rule);padding-bottom:2px;color:var(--muted)}
  .checks{position:absolute;left:16px;top:220px;width:298px;display:flex;justify-content:space-between;font-size:5px;color:var(--muted)}
  .checks span::before{content:"";display:inline-block;width:6px;height:6px;border:1px solid var(--muted);margin-right:3px;vertical-align:-1px}

  /* envelopes */
  .envelope{width:430px;height:108px}
  .envelope.back{left:748px;top:40px}
  .envelope.back svg{position:absolute;inset:0}
  .envelope.front{left:748px;top:176px}
  .envelope.front .band{top:12px;width:300px;height:14px;line-height:14px}
  .envelope .brand{left:14px;top:34px;font-size:15px}
  .envelope .brand .dot{width:20px;height:20px}
  .envelope .address{position:absolute;left:170px;top:44px;font-size:5px;color:var(--muted)}
  .envelope .web{position:absolute;right:14px;top:44px;font-size:5px;color:var(--muted)}

  /* business cards */
  .card{top:360px;width:138px;height:74px;border-radius:37px}
  .card.front{left:740px}
  .card.back-a{left:890px}
  .card.back-b{left:1040px}
  .card .edge{position:absolute;left:0;top:0;bottom:0;width:14px;background:linear-gradient(180deg,var(--blue-light),var(--blue))}
  .card .edge::after{content:"";position:absolute;right:-3px;top:0;bottom:0;width:3px;background:var(--green)}
  .card.front .brand{left:22px;top:26px;font-size:14px}
  .card.front .brand .dot{width:18px;height:18px}
  .card .person{position:absolute;right:14px;top:14px;text-align:right;font-size:5px;line-height:1.5;color:var(--muted)}
  .card .person b{color:var(--ink);font-size:6px}
  .card .contact{position:absolute;right:14px;bottom:12px;text-align:right;font-size:4.5px;line-height:1.5;color:var(--muted)}
</style>
</head>
<body>
<div class="canvas">

  <section class="sheet letterhead">
    <div class="brand"><span class="dot"></span><span>varkomo.de<small>Online-Dienstleistungen</small></span></div>
    <div class="band">Ulmenhain Str. 14 · 70386 Weil der Stadt · tobias.wendrich@mailhafen.de</div>
    <div class="faint-mark">varkomo.de</div>
  </section>

  <section class="sheet fax">
    <div class="brand"><span class="dot"></span><span>varkomo.de<small>Online-Dienstleistungen</small></span></div>
    <div class="band">Ulmenhain Str. 14 · 70386 Weil der Stadt · tobias.wendrich@mailhafen.de</div>
    <h1>FAX</h1>
    <div class="fax-fields">
      <div class="field">To:</div><div class="field">From:</div>
      <div class="field">Fax:</div><div class="field">Pages:</div>
      <div class="field">Phone:</div><div class="field">Date:</div>
      <div class="field">Re:</div><div class="field">CC:</div>
    </div>
    <div class="checks">
      <span>Urgent</span><span>For Review</span><span>Please Comment</span><span>Please Reply</span><span>Please Recycle</span>
    </div>
  </section>

  <section class="envelope back">
    <svg width="430" height="108" viewBox="0 0 430 108" aria-hidden="true">
      <path d="M0 0 L215 62 L430 0" fill="none" stroke="#d5d9dd" stroke-width="1"/>
      <path d="M0 108 L170 50 M430 108 L260 50" fill="none" stroke="#e3e6e9" stroke-width="1"/>
    </svg>
  </section>

  <section class="envelope front">
    <div class="band">www.varkomo.de</div>
    <div class="brand"><span class="dot"></span><span>varkomo.de<small>Online-Dienstleistungen</small></span></div>
    <div class="address">Ulmenhain Str. 14 · 70386 Weil der Stadt</div>
    <div class="web">www.varkomo.de</div>
  </section>

  <section class="card front">
    <div class="edge"></div>
    <div class="brand"><span class="dot"></span><span>varkomo.de<small>Online-Dienstleistungen</small></span></div>
  </section>

  <section class="card back-a">
    <div class="edge"></div>
    <div class="person"><b>Tobias Wendrich</b><br>Dipl. Inf. · Luvesor</div>
    <div class="contact">Ulmenhain Str. 14, 70386 Weil der Stadt<br>Tel. +49 7033 5180 22<br>tobias.wendrich@mailhafen.de</div>
  </section>

  <section class="card back-b">
    <div class="edge"></div>
    <div class="person"><b>Tobias Wendrich</b><br>Dipl. Inf. · Brava Tenq</div>
    <div class="contact">Fax +49 7033 5180 23<br>www.varkomo.de<br>tobias.wendrich@mailhafen.de</div>
  </section>

</div>
</body>
</html>
```